HTML Digital Sign layout and code (one page)...save us from the 60's!

Digital Sign for Headquarters Entrance

HTML Digital Sign layout (one page)...save us from the 60's!

Good Day Designers!

We have decided to install Digital Signage in our headquarters building that will replace the “felt boards” that the administrative staff use at our building entrances.

Instead of the information being displayed on the archaic sign boards, it will be presented on a landscaped 50inch LCD screen running at 1920x1080

We are looking for a one page HTML design that encompass the following elements:

+ Our Logo
+ Our Company Name (HRV Solvance)
+ Our "Tag Line" - "Precision Guided By Experience, Quality Guided By Dedication"
+ Date and Time
+ A space for Today’s Birthdays (which could be up to 4 people)
+ A space for Today’s Anniversaries (which could be up to 4 people)
+ A space for Today’s Visitor (which could be up to 2 people)
+ A space for a Picture of the Day
+ A space for Weather Forecast (perhaps a graphic)
+ A small "banner" section or strip for scrolling Notices / Alerts (perhaps at the bottom of the page?)

The deliverables for the layout need to include the HTML, applicable CSS, HTML code, etc. We need this to be relatively turnkey.

I have included in the contest package a hi-res JPG and AI for our Company Logo.

From a color pallet perspective:

Light Blue:
RGB - 21, 191,242
HEX - #15BFF2

Dark Blue:
RGB - 0, 70, 154
HEX - #00469A

Additionally, I have done a contest like this before (for another company I was at) and have included a screen shot of that final display.

PLEASE NOTE: IT DOES NOT HAVE TO LOOK EXACTLY LIKE THE ATTACHED SCREEN SHOT FROM THE PREVIOUS CONTEST. Including the screenshot was just to give you a general idea of some inspiration and objectives.

Feedback and questions are encouraged.

Target Market(s)

Our Employees

Industry/Entity Type

Digital

Number of Pages Required

1 page

Requirements
Must have
• + Our Logo
• + Our Company Name (HRV Solvance)
• + Our "Tag Line" - "Precision Guided By Experience, Quality Guided By Dedication"
• + Date and Time
• + A space for Today’s Birthdays (which could be up to 4 people)
• + A space for Today’s Anniversaries (which could be up to 4 people)
• + A space for Today’s Visitor (which could be up to 2 people)
• + A space for a Picture of the Day
• + A space for Weather Forecast (perhaps a graphic)
• + A small "banner" section or strip for scrolling Notices / Alerts (perhaps at the bottom of the page?)

```html
<!DOCTYPE html>
<html lang="en">
<head>
<meta charset="utf-8">
<title>HRV Solvance — Entrance Display</title>
<link rel="stylesheet" href="https://fonts.googleapis.com/css2?family=Lato:wght@400;700&family=EB+Garamond:ital@0;1&display=swap">
<style>
  :root {
    --brand-blue: #1428d0;
    --title-blue: #1f74e6;
    --navy: #0b2a9e;
    --navy-dark: #0a1f86;
    --row-blue: #cfe5fb;
    --row-line: #eef6fe;
    --panel-white: #ffffff;
    --ink: #1f2226;
    --ink-soft: #2e3238;
    --bg-left: #b3dbfb;
    --bg-right: #86b3ee;
  }
  * { box-sizing: border-box; margin: 0; padding: 0; }
  html, body { width: 1200px; height: 731px; overflow: hidden; }
  body {
    position: relative;
    font-family: "Lato", sans-serif;
    color: var(--ink);
    background: linear-gradient(100deg, var(--bg-left) 0%, #a2cdf8 45%, var(--bg-right) 100%);
  }

  /* Header */
  .masthead { position: absolute; left: 0; top: 0; width: 1200px; height: 220px; }
  .masthead__photo {
    position: absolute; inset: 0;
    background:
      linear-gradient(90deg, #f2f0ee 0%, #ebe7e2 22%, rgba(235,231,226,0.5) 36%, rgba(235,231,226,0) 48%),
      radial-gradient(ellipse at 62% 55%, #9a9ca2 0%, #7e7468 18%, transparent 40%),
      linear-gradient(180deg, #8c7a64 0%, #a58c6c 45%, #6a5a48 100%);
  }
  .masthead__strip {
    position: absolute; left: 0; top: 220px; width: 1200px; height: 14px;
    background: linear-gradient(90deg, rgba(255,255,255,0.55), rgba(255,255,255,0.25));
  }
  .brand { position: absolute; left: 20px; top: 20px; }
  .brand__name {
    font-family: "Lato", sans-serif; font-weight: 700;
    font-size: 52px; line-height: 1; color: var(--brand-blue);
    letter-spacing: 1px;
  }
  .tagline { position: absolute; left: 18px; top: 142px; font-family: "EB Garamond", serif; color: #151515; }
  .tagline__first { font-style: italic; font-size: 24px; display: block; }
  .tagline__second { font-size: 30px; display: block; margin-top: 0; }

  /* Date & weather */
  .date-tab {
    position: absolute; left: 836px; top: 200px; width: 230px; height: 46px;
    background: var(--navy);
    clip-path: polygon(0 0, 100% 0, 100% 100%, 10px 100%);
    display: flex; align-items: center; gap: 12px; padding-left: 18px;
  }
  .date-tab__group { display: flex; gap: 3px; }
  .date-tab__digit {
    width: 16px; height: 28px; background: linear-gradient(#ffffff, #e4e8ee);
    border-radius: 2px; font-size: 17px; color: #222;
    display: flex; align-items: center; justify-content: center;
  }
  .weather {
    position: absolute; left: 1062px; top: 196px; width: 138px; height: 56px;
    background: var(--navy-dark); color: #fff;
  }
  .weather__icon { position: absolute; left: 24px; top: 4px; }
  .weather__temp { position: absolute; left: 58px; top: 4px; font-size: 20px; font-weight: 700; }
  .weather__units { position: absolute; left: 86px; top: 8px; font-size: 11px; }
  .weather__place { position: absolute; left: 28px; top: 37px; font-size: 13px; }

  /* Panels */
  .panel { position: absolute; background: var(--row-blue); box-shadow: 0 1px 4px rgba(40,80,140,0.18); }
  .panel__head {
    height: 62px; background: var(--panel-white);
    display: flex; align-items: center; gap: 12px; padding-left: 12px;
  }
  .panel__title { font-size: 24px; font-weight: 700; color: var(--title-blue); letter-spacing: 0.2px; }
  .anniversaries .panel__title { font-size: 23.5px; }
  .roster { list-style: none; }
  .roster__row { display: flex; height: 42px; border-top: 2px solid var(--row-line); }
  .roster__row:first-child { border-top: none; }
  .roster__num { width: 47px; border-right: 2px solid var(--row-line); font-size: 15px; padding: 9px 0 0 14px; color: var(--ink-soft); }
  .roster__name { font-size: 17.5px; padding: 9px 0 0 20px; }

  .birthdays { left: 18px; top: 284px; width: 363px; height: 229px; }
  .anniversaries { left: 419px; top: 284px; width: 362px; height: 229px; }
  .news { left: 819px; top: 284px; width: 362px; height: 229px; }
  .visitors { left: 18px; top: 551px; width: 363px; height: 145px; }
  .notices { left: 419px; top: 551px; width: 762px; height: 145px; }

  .news__item { position: relative; height: 80px; padding: 12px 22px 0 82px; }
  .news__item + .news__item { height: 78px; padding-top: 8px; }
  .news__date {
    position: absolute; left: 15px; top: 12px; width: 48px; height: 58px;
    background: var(--navy-dark); color: #fff; text-align: center;
  }
  .news__item + .news__item .news__date { top: 8px; }
  .news__day { font-size: 22px; font-weight: 700; line-height: 34px; display: block; }
  .news__month { font-size: 14px; display: block; border-top: 1px solid #3e56b8; line-height: 22px; }
  .news__headline { font-size: 17px; font-weight: 400; color: var(--title-blue); line-height: 20px; white-space: nowrap; }
  .news__body { font-size: 13.5px; line-height: 22px; color: var(--ink); }

  .notices__head { background: linear-gradient(90deg, #fff 70%, #eef5fd); }
  .notices__text { padding: 8px 30px 0 22px; font-size: 16px; line-height: 29px; color: var(--ink); }
</style>
</head>
<body>
  <header class="masthead">
    <div class="masthead__photo" role="img" aria-label="Photo of a passenger jet inside a maintenance hangar"></div>
    <div class="brand"><div class="brand__name">HRV Solvance</div></div>
    <p class="tagline">
      <span class="tagline__first">Precision Guided By Experience,</span>
      <span class="tagline__second">Quality Guided By Dedication</span>
    </p>
  </header>
  <div class="masthead__strip"></div>

  <div class="date-tab" aria-label="08 Feb 2014">
    <div class="date-tab__group"><span class="date-tab__digit">0</span><span class="date-tab__digit">8</span></div>
    <div class="date-tab__group"><span class="date-tab__digit">F</span><span class="date-tab__digit">E</span><span class="date-tab__digit">B</span></div>
    <div class="date-tab__group"><span class="date-tab__digit">2</span><span class="date-tab__digit">0</span><span class="date-tab__digit">1</span><span class="date-tab__digit">4</span></div>
  </div>
  <div class="weather">
    <svg class="weather__icon" width="28" height="28" viewBox="0 0 28 28" fill="none" stroke="#fff" stroke-width="1.6">
      <circle cx="10" cy="10" r="4"/>
      <path d="M10 2v2M2 10h2M4.5 4.5l1.4 1.4M15.5 4.5l-1.4 1.4"/>
      <path d="M9 20a4 4 0 0 1 1-7.8 5 5 0 0 1 9.5 1.3A3.3 3.3 0 0 1 19 20z" fill="var(--navy-dark)"/>
      <path d="M11 23l-1 3M15 23l-1 3M19 23l-1 3"/>
    </svg>
    <span class="weather__temp">25</span>
    <span class="weather__units">°C | °F</span>
    <span class="weather__place">San Antonio, TX</span>
  </div>

  <section class="panel birthdays">
    <div class="panel__head">
      <svg width="36" height="36" viewBox="0 0 36 36" fill="var(--navy)">
        <rect x="17" y="2" width="2" height="6" rx="1" fill="#f2a23a"/>
        <rect x="11" y="10" width="14" height="7" rx="1"/>
        <rect x="7" y="18" width="22" height="7" rx="1"/>
        <rect x="3" y="26" width="30" height="8" rx="1"/>
        <path d="M7 21h22M3 29h30" stroke="#fff" stroke-width="1"/>
      </svg>
      <h2 class="panel__title">TODAY’S BIRTHDAYS</h2>
    </div>
    <ul class="roster">
      <li class="roster__row"><span class="roster__num">(1)</span><span class="roster__name">Mr. Owen Carter Hollis</span></li>
      <li class="roster__row"><span class="roster__num">(2)</span><span class="roster__name">Mr. Marcus Reid Fenwick</span></li>
      <li class="roster__row"><span class="roster__num">(3)</span><span class="roster__name">Ms. Clara Renee Whitford</span></li>
      <li class="roster__row"><span class="roster__num">(4)</span><span class="roster__name">Ms. Nora Ellis Brandt</span></li>
    </ul>
  </section>

  <section class="panel anniversaries">
    <div class="panel__head">
      <svg width="36" height="36" viewBox="0 0 36 36">
        <path d="M10 22l-4 12 5-2 3 4 3-11zM26 22l4 12-5-2-3 4-3-11z" fill="var(--navy)"/>
        <circle cx="18" cy="14" r="12" fill="var(--navy)"/>
        <circle cx="18" cy="14" r="8" fill="none" stroke="#fff" stroke-width="1.5"/>
        <path d="M18 9l1.5 3.2 3.4.4-2.5 2.3.7 3.4-3.1-1.7-3.1 1.7.7-3.4-2.5-2.3 3.4-.4z" fill="#fff"/>
      </svg>
      <h2 class="panel__title">TODAY’S ANNIVERSARIES</h2>
    </div>
    <ul class="roster">
      <li class="roster__row"><span class="roster__num">(1)</span><span class="roster__name">Mr. Victor Hale Moreno</span></li>
      <li class="roster__row"><span class="roster__num">(2)</span><span class="roster__name">Mr. Ethan Lowell Pryce</span></li>
      <li class="roster__row"><span class="roster__num">(3)</span><span class="roster__name">Mr. Calvin Marsh</span></li>
      <li class="roster__row"><span class="roster__num">(4)</span><span class="roster__name">Mr. Peter Oakridge</span></li>
    </ul>
  </section>

  <section class="panel news">
    <div class="panel__head">
      <svg width="44" height="36" viewBox="0 0 44 36" fill="var(--navy)">
        <rect x="6" y="2" width="36" height="32" rx="2"/>
        <path d="M6 10H2v22a2 2 0 0 0 4 0z"/>
        <rect x="10" y="7" width="28" height="5" fill="#fff"/>
        <rect x="10" y="15" width="12" height="13" fill="#fff"/>
        <path d="M25 16h13M25 21h13M25 26h13" stroke="#fff" stroke-width="2"/>
      </svg>
      <h2 class="panel__title">HRV News</h2>
    </div>
    <article class="news__item">
      <div class="news__date"><span class="news__day">11</span><span class="news__month">SEP</span></div>
      <h3 class="news__headline">Adipiscing elit sed diam nonumm</h3>
      <p class="news__body">Lorem ipsum dolor sitl auer adipiscingm elit diam nonum mymi nibh sod tidun.</p>
    </article>
    <article class="news__item">
      <div class="news__date"><span class="news__day">12</span><span class="news__month">SEP</span></div>
      <h3 class="news__headline">Utwisi enim ad minim veniamuis</h3>
      <p class="news__body">Lorem ipsum dolor sitl auer adipiscingm elit diam nonum mymi nibh sod tidun.</p>
    </article>
  </section>

  <section class="panel visitors">
    <div class="panel__head">
      <svg width="36" height="36" viewBox="0 0 36 36" fill="var(--navy)">
        <circle cx="18" cy="10" r="7"/>
        <path d="M4 34c0-8 6-13 14-13s14 5 14 13z"/>
        <path d="M18 21l-2 3 2 8 2-8z" fill="#fff"/>
      </svg>
      <h2 class="panel__title">TODAY’S VISITOR</h2>
    </div>
    <ul class="roster">
      <li class="roster__row"><span class="roster__num">(1)</span><span class="roster__name">Mr. Owen Carter Hollis</span></li>
      <li class="roster__row"><span class="roster__num">(2)</span><span class="roster__name">Mr. Marcus Reid Fenwick</span></li>
    </ul>
  </section>

  <section class="panel notices">
    <div class="panel__head notices__head">
      <svg width="36" height="32" viewBox="0 0 36 32" fill="var(--navy)">
        <rect x="2" y="11" width="6" height="10"/>
        <path d="M9 11l18-9v28L9 21z"/>
        <path d="M11 22h6l2 9h-5z"/>
        <path d="M30 12v8" stroke="var(--navy)" stroke-width="3" stroke-linecap="round"/>
      </svg>
      <h2 class="panel__title">NOTICES</h2>
    </div>
    <p class="notices__text">Lorem ipsum dolor sit amet consectetuer adipiscing elit sedm nonu mmymi nibh euismod hui<br>elit sedm nonu mmymi nibtincidunt ut laoreet dolore magna aliquam erat.</p>
  </section>
</body>
</html>
```